Harborline Open Cinema Gathering 20th Annual Poster

September 2017 will to the 20th Annual Harborline Open Cinema Gathering. We have a new logo and need a new modern stylish poster designed. One that shows creativity, imagination, style and class. Think outside the box. Modern and new.

Dates are: September 7th - 13th 2017

Our tagline:
"Something for Everyone from Around the World"

Target Market(s)

film festival goings - 35 - 70 age range - 58% female 42% males - movie lovers - movie goers

Industry/Entity Type

Movie

Font styles to use
Script

Requirements
Must have
• modern style celebrating 20 years - cool design - chic and stylish - upscale - high society - think Abstract
Nice to have
• thinking outside the box - not just simple film reel - think Abstract! Not just your standard film items. Creative in your idea and design
Should not have
• no CLIP ART

```html
<!DOCTYPE html>
<html lang="en">
<head>
<meta charset="utf-8">
<title>Harborline Open Cinema Gathering – 20th Annual</title>
<link rel="stylesheet" href="https://fonts.googleapis.com/css2?family=Archivo+Black&family=Montserrat:wght@600;700&display=swap">
<style>
  :root {
    --sky-top: #c6cdd6;
    --sky-bottom: #f5f6f8;
    --headline-light: #3563b0;
    --headline-dark: #1a2f66;
    --navy: #14204a;
    --carpet: #0f2150;
    --white: #ffffff;
    --chair-light: #e4e8ee;
    --chair-blue: #1f2f86;
    --globe-blue: #283a9a;
    --globe-green: #3dbb4a;
    --reel-light: #5a8fd0;
    --reel-dark: #0d1733;
  }
  * { margin: 0; padding: 0; box-sizing: border-box; }
  html, body { width: 849px; height: 1200px; overflow: hidden; }
  body { background: var(--sky-bottom); }
  .poster {
    position: relative;
    width: 849px;
    height: 1200px;
    overflow: hidden;
    background: linear-gradient(180deg, var(--sky-top) 0%, var(--sky-bottom) 70%);
  }
  .scene { position: absolute; inset: 0; }
  .tagline {
    position: absolute;
    right: 54px;
    top: 28px;
    text-align: right;
    white-space: nowrap;
    font-family: "Archivo Black", "Arial Black", sans-serif;
    font-weight: 400;
    font-size: 79px;
    line-height: 88px;
    text-transform: uppercase;
    background: linear-gradient(180deg, var(--headline-light), var(--headline-dark));
    -webkit-background-clip: text;
    background-clip: text;
    color: transparent;
  }
  .edition {
    position: absolute;
    right: 54px;
    top: 396px;
    text-align: right;
    white-space: nowrap;
    color: var(--white);
    font-family: "Montserrat", Arial, sans-serif;
    font-weight: 600;
    text-transform: uppercase;
  }
  .edition__year { font-size: 31px; line-height: 34px; }
  .edition__year sup { font-size: 17px; vertical-align: 12px; text-transform: none; }
  .edition__name { font-size: 20px; line-height: 24px; }
  .edition__kind { font-size: 34px; line-height: 38px; }
  .dates {
    position: absolute;
    right: 54px;
    top: 510px;
    text-align: right;
    white-space: nowrap;
    color: var(--navy);
    font-family: "Archivo Black", "Arial Black", sans-serif;
    font-size: 37px;
    line-height: 36px;
  }
  .festival-mark {
    position: absolute;
    left: 616px;
    top: 661px;
    width: 182px;
    height: 132px;
    background: var(--navy);
    display: flex;
    flex-direction: column;
    align-items: center;
    justify-content: center;
    gap: 10px;
  }
  .festival-mark__dot {
    width: 30px;
    height: 30px;
    border-radius: 50%;
    background: var(--globe-green);
  }
  .festival-mark__name {
    color: var(--white);
    font-family: "Montserrat", Arial, sans-serif;
    font-weight: 700;
    font-size: 30px;
    letter-spacing: 3px;
  }
</style>
</head>
<body>
  <main class="poster">
    <svg class="scene" width="849" height="1200" viewBox="0 0 849 1200" xmlns="http://www.w3.org/2000/svg">
      <defs>
        <linearGradient id="chairTone" x1="0" y1="0" x2="1" y2="1">
          <stop offset="0" stop-color="var(--chair-light)"/>
          <stop offset="0.5" stop-color="var(--chair-blue)" stop-opacity="0.55"/>
          <stop offset="1" stop-color="var(--chair-light)"/>
        </linearGradient>
        <radialGradient id="globeTone" cx="0.55" cy="0.55" r="0.6">
          <stop offset="0" stop-color="var(--globe-blue)"/>
          <stop offset="0.7" stop-color="var(--globe-green)" stop-opacity="0.8"/>
          <stop offset="1" stop-color="var(--navy)"/>
        </radialGradient>
        <linearGradient id="reelTone" x1="0" y1="0" x2="1" y2="1">
          <stop offset="0" stop-color="var(--reel-light)"/>
          <stop offset="1" stop-color="var(--reel-dark)"/>
        </linearGradient>
      </defs>
      <polygon class="scene__chair" points="40,396 392,396 392,566 608,584 608,760 540,790 540,1104 40,1104" fill="url(#chairTone)" role="img" aria-label="Director's chair with navy canvas seat and white wooden frame"/>
      <polygon class="scene__carpet" points="152,860 704,860 849,1200 0,1200" fill="var(--carpet)"/>
      <circle class="scene__globe" cx="410" cy="626" r="152" fill="url(#globeTone)" role="img" aria-label="Blue and green globe resting on the chair seat"/>
      <rect class="scene__reel" x="252" y="836" width="596" height="236" rx="30" fill="url(#reelTone)" role="img" aria-label="Curling strip of film unspooling across the carpet"/>
    </svg>

    <h1 class="tagline">Something<br>for everyone<br>from around<br>the world</h1>

    <div class="edition">
      <div class="edition__year">20<sup>th</sup> Annual</div>
      <div class="edition__name">Harborline Open Cinema</div>
      <div class="edition__kind">Gathering</div>
    </div>

    <div class="dates">SEPTEMBER<br>7th - 13th<br>2017</div>

    <div class="festival-mark">
      <span class="festival-mark__dot"></span>
      <span class="festival-mark__name">HOCG</span>
    </div>
  </main>
</body>
</html>
```